SALTBUSH COMPUTERS AD DESIGN

This is to go into our local phone book as a full page (A4) advert.

NOTE THAT THE DEADLINE IS MIDNIGHT SUNDAY THE 29TH AUSSIE WA TIME NOT THE ADVERTISED DEADLINE AS FOR THE LIFE OF ME I CANT SEE WHERE TO CHANGE IT.

HAPPY TO PAY EXTRA FOR A "YES THATS IT" JOB.

Title - SALTBUSH COMPUTERS

(THINGS TO HAVE)
24/7 FULL COMPUTER SERVICES
ALL COMPUTER PROBLEMS SOLVED
info@saltbushcomputers.com.au
0400 12 5836
SALTBUSHCOMPUTERS.COM.AU
Virus's Removed
Data Recovery
Custom Computers and Programs built
Picked up & Dropped off
Private and Business Welcome

Maybe this photo - http://www.framelyart.com/stock-photo-20573142-attractive-receptionist.php?st=a3e81c5
with 24/7 service.

http://www.framelyart.com/stock-photo-20591736-hard-disk-drive-service.php?st=d74f2a9 with Data Recovery

http://www.framelyart.com/stock-illustration-3862517-laptop.php?st=5e1b8f2

I don't know but I have less than 40 hours to do this...

Been extented for another 50 hours cause they stuffed up also I have just opened a logo one as well.

Reason: As the publisher stuffed up with my account I now have an extra 50 hours !!

please note increased payment, this may increase again.

Reason: Not ment to finish for another 18 hours !!!!!!

Keep Going !!!!

only 5 hours left before it has to be at the printers !!!!

Industry/Entity Type

Business

Requirements
Must have
• only have 40 hours left from now. it must be in by 7am Monday 30th western aussie time. (not eastern aussie time)
Nice to have
• A 3D look
Colors like dark blue, bright yellow black and dark red.
modern look
modern font ie..HandelGothicBT etc

```html
<!DOCTYPE html>
<html lang="en">
<head>
<meta charset="utf-8">
<title>Saltbush Computers – Full Page Advert</title>
<link rel="stylesheet" href="https://fonts.googleapis.com/css2?family=Fira+Sans:wght@600;700&display=swap">
<style>
  :root {
    --red: #e3141b;
    --red-deep: #9e0d12;
    --black: #221f1f;
    --white: #ffffff;
    --text-font: "Fira Sans", Arial, sans-serif;
  }
  html, body {
    margin: 0;
    padding: 0;
    overflow: hidden;
    background: var(--white);
  }
  .advert {
    position: relative;
    width: 850px;
    height: 1200px;
    overflow: hidden;
    background: var(--red);
    font-family: var(--text-font);
  }
  .advert__backdrop {
    position: absolute;
    inset: 0;
  }
  .advert__text {
    position: absolute;
    margin: 0;
    white-space: nowrap;
  }
  .brand-name {
    left: 360px;
    width: 500px;
    top: 190px;
    text-align: center;
    color: var(--red);
    font-weight: 700;
    font-size: 80px;
    line-height: 88px;
  }
  .service-list {
    position: absolute;
    left: 340px;
    width: 490px;
    top: 430px;
    margin: 0;
    padding: 0;
    list-style: none;
    text-align: center;
    color: var(--white);
    font-weight: 600;
  }
  .service-list__item {
    font-size: 23px;
    line-height: 48px;
  }
  .service-list__item--lead {
    font-weight: 700;
    font-size: 25px;
  }
  .pickup-note {
    left: 33px;
    top: 666px;
    color: var(--red);
    font-weight: 700;
    font-size: 21px;
  }
  .contact-block {
    position: absolute;
    left: 33px;
    top: 994px;
    margin: 0;
    font-style: normal;
    font-size: 20px;
    line-height: 34px;
  }
  .contact-block__welcome,
  .contact-block__web {
    color: var(--red);
    font-weight: 700;
  }
  .contact-block__email {
    color: var(--white);
    font-weight: 600;
  }
  .contact-block__phone {
    color: var(--white);
    font-weight: 700;
  }
  .contact-block span { display: block; }
</style>
</head>
<body>
<main class="advert">
  <svg class="advert__backdrop" width="850" height="1200" viewBox="0 0 850 1200">
    <defs>
      <linearGradient id="mosaicFill" x1="0" y1="0" x2="1" y2="1">
        <stop offset="0" stop-color="#e3141b"/>
        <stop offset="1" stop-color="#8e0c10"/>
      </linearGradient>
      <linearGradient id="artFill" x1="0" y1="0" x2="1" y2="1">
        <stop offset="0" stop-color="#9fb3c9"/>
        <stop offset="1" stop-color="#5f7690"/>
      </linearGradient>
    </defs>

    <rect class="mosaic-panel" x="0" y="0" width="205" height="410" fill="url(#mosaicFill)"
          role="img" aria-label="Decorative mosaic of red squares"/>
    <rect class="mosaic-panel" x="600" y="765" width="250" height="435" fill="url(#mosaicFill)"
          role="img" aria-label="Decorative mosaic of red squares"/>

    <circle class="hero-circle" cx="560" cy="360" r="390" fill="var(--black)" stroke="var(--white)" stroke-width="6"/>
    <circle class="contact-circle" cx="190" cy="900" r="340" fill="var(--black)" stroke="var(--white)" stroke-width="6"/>
    <circle class="hero-circle__ring" cx="560" cy="360" r="372" fill="none" stroke="var(--red)" stroke-width="4"/>

    <g class="service-dividers" stroke="var(--red)" stroke-width="3">
      <line x1="385" y1="472" x2="786" y2="472"/>
      <line x1="478" y1="520" x2="690" y2="520"/>
      <line x1="390" y1="564" x2="776" y2="564"/>
      <line x1="358" y1="615" x2="806" y2="615"/>
    </g>

    <ellipse class="divider-flourish" cx="588" cy="676" rx="48" ry="9" fill="var(--red-deep)"
             role="img" aria-label="Small decorative flourish"/>

    <rect class="technician-art" x="28" y="704" width="368" height="254" rx="10" fill="url(#artFill)"
          role="img" aria-label="Illustration of two cartoon computer towers repairing each other with a screwdriver and a circuit board"/>
  </svg>

  <h1 class="advert__text brand-name">Saltbush<br>Computers</h1>

  <ul class="service-list">
    <li class="service-list__item service-list__item--lead">24/7 FULL COMPUTER SERVICES</li>
    <li class="service-list__item">Virus's Removed</li>
    <li class="service-list__item">All Computer Problems Solved</li>
    <li class="service-list__item">Custom Computers &amp; Programs built</li>
    <li class="service-list__item">Data Recovery</li>
  </ul>

  <p class="advert__text pickup-note">Picked up &amp; Dropped off</p>

  <address class="contact-block">
    <span class="contact-block__welcome">Private and Business Welcome</span>
    <span class="contact-block__email">info@saltbushcomputers.com.au</span>
    <span class="contact-block__web">saltbushcomputers.com.au</span>
    <span class="contact-block__phone">0400 12 5836</span>
  </address>
</main>
</body>
</html>
```